Website design for legal tech start up in Switzerland (B2B)

We are for a legal tech start up in Switzerland called TAVO. We have been running since August 2016. This will be our first live website.

We need a website designed and business card design for our start-up in Switzerland. We also need the Web design to be converted into HTML and CSS files.

Function of website:
• To inform potential customers of our services
• Form a key part of our digital marketing and sales footprint.
• Branding

Please find attached logo.
Updates

Project Deadline Extended Reason: Giving us time to review submissions and provide opportunity for more submissions. Added Thursday, February 16, 2017

Reason: Looking for more idea's not necessarily set on blue and grey colours only.

Target Market(s)

B2B tech powered legal services.

Industry/Entity Type

Legal

Contact Information for Business Card

Lean and slick design.

Coding

Coded - Design and coding required

Number of Pages Required

5+ page

Requirements
Must have
• VERY LEAN AND CLEAN DESIGN!
• We have received many great standard designs, but we are looking for something more out-of-the box: You can get inspiration from these designs: http://www.pindelsite.com/websites/clean/
• Thanks!!
• Easy content management system
• Well structured coding for additional development
• Responsive webpage for all types of devices
• SEO optimized
• Tabs (Home, services, team, careers, blog, contact us)
• Colour scheme complementary to logo
Nice to have
• Look and Design - Approachable, High-tech, Modern
• Easy to add chat bot capability in future
Should not have
• Too busy/ too much clutter
• Not take to long to load

```html
<!DOCTYPE html>
<html lang="en">
<head>
<meta charset="utf-8">
<title>TAVO – Legal Services</title>
<link href="https://fonts.googleapis.com/css2?family=Open+Sans:wght@400;600;700&display=swap" rel="stylesheet">
<style>
:root{
  --navy:#1b3a6b;
  --navy-dark:#163260;
  --text:#333;
  --muted:#8a8a8a;
  --light:#f5f5f5;
  --line:#cfcfcf;
  --footer:#454545;
  --footer-text:#d6d6d6;
  --white:#fff;
}
*{box-sizing:border-box;margin:0;padding:0}
html,body{width:1200px;height:2691px;overflow:hidden}
body{font-family:'Open Sans',Arial,sans-serif;color:var(--text);background:var(--white);position:relative}
.abs{position:absolute}
.section{position:absolute;left:0;width:1200px}
.section-title{position:absolute;left:0;width:1200px;text-align:center;font-size:24px;font-weight:700;color:var(--navy);letter-spacing:.5px}

/* header */
.site-header{top:0;height:109px;background:var(--white)}
.brand{left:131px;top:24px;font-size:44px;font-weight:700;color:#2b3f5c;letter-spacing:2px;line-height:60px}
.main-nav{right:133px;top:46px;display:flex;gap:29px;font-size:11px;text-transform:uppercase;color:#555}
.main-nav .active{color:var(--navy);font-weight:700}

/* hero */
.hero{top:109px;height:503px;background:linear-gradient(180deg,#7fa6d6 0%,#b7cfe9 30%,#e8eef5 62%,#dfe6ef 100%)}
.hero-arrow{top:236px;width:24px;height:32px;background:#333;display:flex;align-items:center;justify-content:center}

/* welcome */
.welcome{top:612px;height:333px}
.welcome .section-title{top:72px}
.welcome-text{left:131px;top:117px;width:938px;text-align:center;font-size:11.5px;line-height:20px;color:#555}
.btn-outline{position:absolute;border:1px solid var(--line);background:var(--white);color:#555;font-size:11px;display:flex;align-items:center;justify-content:center}

/* services */
.services{top:945px;height:406px;background:var(--light)}
.services .section-title{top:71px}
.service{position:absolute;top:143px;width:240px;text-align:center}
.service svg{display:block;margin:0 auto}
.service h3{margin-top:12px;font-size:21px;font-weight:400;color:var(--navy);letter-spacing:.3px}
.service p{margin-top:6px;font-size:10px;line-height:16px;color:#666;padding:0 6px}
.service .btn-outline{position:relative;margin:14px auto 0;width:82px;height:37px;font-size:9px;text-transform:uppercase}

/* contact */
.contact{top:1351px;height:237px;background:var(--navy)}
.contact .section-title{top:74px;color:var(--white)}
.field{position:absolute;top:113px;height:43px;background:#f3f4f6;font-size:11px;color:#666;padding:0 24px;display:flex;align-items:center}
.submit{position:absolute;left:816px;top:113px;width:79px;height:43px;background:linear-gradient(#5a5a5a,#2d2d2d);color:var(--white);font-size:12px;font-weight:600;display:flex;align-items:center;justify-content:center}

/* team */
.team{top:1588px;height:305px}
.team .section-title{top:72px}
.member{position:absolute;top:129px;width:440px;height:100px}
.member .photo{position:absolute;left:0;top:0;width:97px;height:95px}
.member h4{position:absolute;left:108px;top:0;font-size:15px;font-weight:600;color:#222}
.member .role{position:absolute;left:108px;top:25px;font-size:11px;color:#333}
.member .bio{position:absolute;left:108px;top:56px;width:332px;font-size:10.5px;line-height:17px;color:var(--muted)}
.member .bio b{color:#222;font-weight:600}

/* blog */
.blog{top:1893px;height:525px;background:var(--light)}
.blog-title{left:131px;top:60px;font-size:24px;font-weight:700;color:var(--navy)}
.blog-nav{top:64px;width:24px;height:22px;border:1px solid #bbb;background:var(--white);display:flex;align-items:center;justify-content:center}
.post{position:absolute;top:115px;width:298px}
.post .thumb{width:298px;height:179px;position:relative}
.post h5{margin-top:16px;font-size:14.5px;font-weight:400;line-height:22px;color:#222}
.post p{margin-top:9px;font-size:10.5px;line-height:17px;color:var(--muted);text-align:justify}
.post .meta{margin-top:14px;display:flex;gap:16px;font-size:10px;color:#555;align-items:center}
.post .meta span{display:flex;align-items:center;gap:5px}

/* footer */
.site-footer{top:2418px;height:273px;background:var(--footer);color:var(--footer-text)}
.footer-head{font-size:15px;color:var(--white)}
.contact-list{list-style:none;font-size:10.5px;line-height:16px}
.contact-list li{display:flex;gap:12px;margin-bottom:10px}
.contact-list svg{flex:none;margin-top:2px}
.map{left:332px;top:74px;width:186px;height:100px;background:linear-gradient(135deg,#eef0f2,#d9dde1)}
.link-list{list-style:none;font-size:10px;line-height:23px}
.link-list li::before{content:"•";margin-right:8px;color:#bbb}
.social{display:flex;flex-wrap:wrap;gap:8px;width:60px}
.social span{width:25px;height:25px;border-radius:50%;background:#6d8fbf;display:block}
.footer-rule{left:0;top:2628px;width:1200px;height:1px;background:#5a5a5a}
.copyright{left:0;top:2650px;width:1200px;text-align:center;font-size:10px;color:var(--footer-text)}
</style>
</head>
<body>

<header class="section site-header">
  <div class="abs brand">TAVO</div>
  <nav class="abs main-nav">
    <span class="active">Home</span><span>Services</span><span>Team</span><span>Careers</span><span>Blog</span><span>Contact us</span>
  </nav>
</header>

<section class="section hero" role="img" aria-label="Snow-covered Alpine mountain peaks under a blue sky with clouds">
  <div class="abs hero-arrow" style="left:0"><svg width="10" height="14"><path d="M8 1 2 7l6 6" stroke="#fff" stroke-width="1.5" fill="none"/></svg></div>
  <div class="abs hero-arrow" style="right:0"><svg width="10" height="14"><path d="M2 1l6 6-6 6" stroke="#fff" stroke-width="1.5" fill="none"/></svg></div>
</section>

<section class="section welcome">
  <h1 class="section-title">WELCOME TO TAVO</h1>
  <p class="abs welcome-text">Donec facilisis volutpat lorem, at euismod velit dignissim ac. Class aptent taciti sociosqu ad litora torquent per conubia nostra, per inceptos himenaeos. Nulla consequat ipsum id mi placerat viverra. Sed tempor ex id dui sagittis, at luctus tortor finibus. Vestibulum ante ipsum primis in faucibus orci luctus et ultrices posuere cubilia Curae; Duis varius condimentum tellus, a faucibus lorem vestibulum eu. Duis sit amet tellus nisl. Maecenas nec metus sodales ante sollicitudin auctor in quis velit. Maecenas libero nisl, dignissim eget nibh a, mollis eleifend tellus. Fusce maximus porttitor libero vitae viverra.</p>
  <div class="btn-outline" style="left:554px;top:215px;width:90px;height:38px">Read more</div>
</section>

<section class="section services">
  <h2 class="section-title">OUR SERVICES</h2>
  <div class="service" style="left:119px">
    <svg width="44" height="40" viewBox="0 0 44 40" fill="#1b3a6b"><circle cx="22" cy="9" r="7"/><circle cx="9" cy="14" r="5"/><circle cx="35" cy="14" r="5"/><path d="M11 36c0-9 5-14 11-14s11 5 11 14z"/><path d="M0 34c0-7 4-11 9-11 2 0 3 .5 4 1-2 3-3 6-3 10z"/><path d="M44 34c0-7-4-11-9-11-2 0-3 .5-4 1 2 3 3 6 3 10z"/></svg>
    <h3>FAMILY LAW</h3>
    <p>Duis varius ante condimentum tellus, faucibus lorem vestibulum eu. Duis sit amet tellus nisl. Maecenas nec metus sodales.</p>
    <div class="btn-outline">Read more</div>
  </div>
  <div class="service" style="left:359px">
    <svg width="44" height="40" viewBox="0 0 44 40" fill="#1b3a6b"><path d="M15 4h14v6h-3V7h-8v3h-3z"/><rect x="1" y="10" width="42" height="28" rx="3"/><rect x="1" y="21" width="42" height="2" fill="#f5f5f5"/><rect x="19" y="18" width="6" height="7" fill="#f5f5f5"/></svg>
    <h3>BUSINESS LAW</h3>
    <p>Duis varius ante condimentum tellus, faucibus lorem vestibulum eu. Duis sit amet tellus nisl. Maecenas nec metus sodales.</p>
    <div class="btn-outline">Read more</div>
  </div>
  <div class="service" style="left:601px">
    <svg width="48" height="40" viewBox="0 0 48 40" fill="#1b3a6b"><path d="M10 6h28l5 14H5z"/><rect x="2" y="18" width="44" height="14" rx="3"/><rect x="5" y="30" width="8" height="8" rx="2"/><rect x="35" y="30" width="8" height="8" rx="2"/><path d="M14 10h20l3 9H11z" fill="#f5f5f5"/><circle cx="10" cy="25" r="3" fill="#f5f5f5"/><circle cx="38" cy="25" r="3" fill="#f5f5f5"/></svg>
    <h3>VEHICLE LAW</h3>
    <p>Duis varius ante condimentum tellus, faucibus lorem vestibulum eu. Duis sit amet tellus nisl. Maecenas nec metus sodales.</p>
    <div class="btn-outline">Read more</div>
  </div>
  <div class="service" style="left:843px">
    <svg width="52" height="40" viewBox="0 0 52 40"><rect x="2" y="6" width="48" height="30" fill="#1b3a6b"/><rect x="7" y="11" width="38" height="20" fill="none" stroke="#f5f5f5" stroke-width="2"/><circle cx="26" cy="21" r="7" fill="#f5f5f5"/><path d="M25 17h2v8h-2z" fill="#1b3a6b"/></svg>
    <h3>DEBT LAW</h3>
    <p>Duis varius ante condimentum tellus, faucibus lorem vestibulum eu. Duis sit amet tellus nisl. Maecenas nec metus sodales.</p>
    <div class="btn-outline">Read more</div>
  </div>
</section>

<section class="section contact">
  <h2 class="section-title">CONTACT US</h2>
  <div class="field" style="left:303px;width:241px">Email</div>
  <div class="field" style="left:560px;width:240px">What is your legal question</div>
  <div class="submit">SUBMIT</div>
</section>

<section class="section team">
  <h2 class="section-title">OUR TEAM</h2>
  <div class="member" style="left:131px">
    <div class="photo" role="img" aria-label="Portrait photo of Mark Elder" style="background:linear-gradient(180deg,#8e8e8e,#4a4a4a)"></div>
    <h4>MARK ELDER</h4>
    <div class="role">Duis sed congue nibh</div>
    <p class="bio">Aenean lobortis neque, vitae faucibus lorem. Nulla dignissim tempus nisi, sed lobortis velit faucibus at. Fusce vel rutrum erat. Vivamus blandit interdum egestas. <b>More</b></p>
  </div>
  <div class="member" style="left:628px">
    <div class="photo" role="img" aria-label="Portrait photo of Clara" style="background:linear-gradient(180deg,#c9b79c,#7d6a55)"></div>
    <h4>CLARA</h4>
    <div class="role">Duis sed congue nibh</div>
    <p class="bio">Aenean lobortis neque, vitae faucibus lorem. Nulla dignissim tempus nisi, sed lobortis velit faucibus at. Fusce vel rutrum erat. Vivamus blandit interdum egestas. <b>More</b></p>
  </div>
</section>

<section class="section blog">
  <h2 class="abs blog-title">BLOG</h2>
  <div class="abs blog-nav" style="left:1013px"><svg width="8" height="10"><path d="M6 1 2 5l4 4" stroke="#777" fill="none"/></svg></div>
  <div class="abs blog-nav" style="left:1043px"><svg width="8" height="10"><path d="M2 1l4 4-4 4" stroke="#777" fill="none"/></svg></div>

  <article class="post" style="left:131px">
    <div class="thumb" role="img" aria-label="Columned courthouse facade under a cloudy sky" style="background:linear-gradient(180deg,#7d98c2 0%,#b9c4d4 45%,#6c6f76 100%)"></div>
    <h5>Donec scelerisque felis at ante rhoncus, non mattis nulla facilisis</h5>
    <p>Integer gravida risus risus, in imperdiet leo convallis sed. Aenean lobortis neque, vitae faucibus lorem. Nulla dignissim tempus nisi, sed lobortis velit faucibus at. Fusce vel rutrum erat. Vivamus blandit interdum egestas.</p>
    <div class="meta">
      <span><svg width="10" height="9" viewBox="0 0 10 9"><path d="M5 9 1 5a2.5 2.5 0 0 1 4-3 2.5 2.5 0 0 1 4 3z" fill="#555"/></svg>(28)</span>
      <span><svg width="10" height="10" viewBox="0 0 10 10"><path d="M0 4h2v6H0zM3 4l3-4c1 0 1.5 1 1 2l-.5 2H10v2l-1.5 4H3z" fill="#555"/></svg>(21)</span>
      <span><svg width="10" height="10" viewBox="0 0 10 10"><rect x=".5" y="1.5" width="9" height="8" fill="none" stroke="#555"/><path d="M.5 4h9" stroke="#555"/></svg>8 Feb, 2017</span>
    </div>
  </article>

  <article class="post" style="left:452px">
    <div class="thumb" role="img" aria-label="Person signing a document with a stamp next to a justice statuette" style="background:linear-gradient(135deg,#e8e8e8 0%,#b5b5b5 50%,#3b3b3b 100%)"></div>
    <h5>Donec scelerisque felis at ante rhoncus, non mattis nulla facilisis</h5>
    <p>Integer gravida risus risus, in imperdiet leo convallis sed. Aenean lobortis neque, vitae faucibus lorem. Nulla dignissim tempus nisi, sed lobortis velit faucibus at. Fusce vel rutrum erat. Vivamus blandit interdum egestas.</p>
    <div class="meta">
      <span><svg width="10" height="9" viewBox="0 0 10 9"><path d="M5 9 1 5a2.5 2.5 0 0 1 4-3 2.5 2.5 0 0 1 4 3z" fill="#555"/></svg>(28)</span>
      <span><svg width="10" height="10" viewBox="0 0 10 10"><path d="M0 4h2v6H0zM3 4l3-4c1 0 1.5 1 1 2l-.5 2H10v2l-1.5 4H3z" fill="#555"/></svg>(21)</span>
      <span><svg width="10" height="10" viewBox="0 0 10 10"><rect x=".5" y="1.5" width="9" height="8" fill="none" stroke="#555"/><path d="M.5 4h9" stroke="#555"/></svg>8 Feb, 2017</span>
    </div>
  </article>

  <article class="post" style="left:770px">
    <div class="thumb" role="img" aria-label="Old town riverside buildings at dusk, video preview" style="background:linear-gradient(180deg,#5c6f8c 0%,#9a7a5e 60%,#3f3a36 100%)">
      <svg class="abs" style="left:129px;top:69px" width="40" height="40" viewBox="0 0 40 40"><circle cx="20" cy="20" r="20" fill="#fff"/><path d="M16 12l12 8-12 8z" fill="#222"/></svg>
    </div>
    <h5>Donec scelerisque felis at ante rhoncus, non mattis nulla facilisis</h5>
    <p>Integer gravida risus risus, in imperdiet leo convallis sed. Aenean lobortis neque, vitae faucibus lorem. Nulla dignissim tempus nisi, sed lobortis velit faucibus at. Fusce vel rutrum erat. Vivamus blandit interdum egestas.</p>
    <div class="meta">
      <span><svg width="10" height="9" viewBox="0 0 10 9"><path d="M5 9 1 5a2.5 2.5 0 0 1 4-3 2.5 2.5 0 0 1 4 3z" fill="#555"/></svg>(28)</span>
      <span><svg width="10" height="10" viewBox="0 0 10 10"><path d="M0 4h2v6H0zM3 4l3-4c1 0 1.5 1 1 2l-.5 2H10v2l-1.5 4H3z" fill="#555"/></svg>(21)</span>
      <span><svg width="10" height="10" viewBox="0 0 10 10"><rect x=".5" y="1.5" width="9" height="8" fill="none" stroke="#555"/><path d="M.5 4h9" stroke="#555"/></svg>8 Feb, 2017</span>
    </div>
  </article>
</section>

<footer class="section site-footer">
  <div class="abs footer-head" style="left:131px;top:42px">Contact info</div>
  <ul class="abs contact-list" style="left:131px;top:78px;width:190px">
    <li><svg width="9" height="11" viewBox="0 0 9 11"><path d="M4.5 11S0 6 0 4.5a4.5 4.5 0 0 1 9 0C9 6 4.5 11 4.5 11z" fill="#ccc"/><circle cx="4.5" cy="4.5" r="1.6" fill="#454545"/></svg><span>24 Building name, Street name<br>City - Zipcode</span></li>
    <li><svg width="9" height="11" viewBox="0 0 9 11"><rect x="1" y="0" width="7" height="11" rx="1.5" fill="#ccc"/><rect x="2.3" y="1.5" width="4.4" height="6.5" fill="#454545"/></svg><span>418 205 7731</span></li>
    <li><svg width="10" height="10" viewBox="0 0 10 10"><rect x="2" y="0" width="6" height="4" fill="#ccc"/><rect x="0" y="3" width="10" height="5" rx="1" fill="#ccc"/><rect x="2" y="6" width="6" height="4" fill="#ccc" stroke="#454545" stroke-width=".8"/></svg><span>418 205 7790</span></li>
    <li><svg width="10" height="8" viewBox="0 0 10 8"><rect width="10" height="8" fill="#ccc"/><path d="M0 0l5 4 5-4" stroke="#454545" fill="none"/></svg><span>info@tavo.ch</span></li>
  </ul>
  <div class="abs map" role="img" aria-label="Street map showing the office location"></div>

  <div class="abs footer-head" style="left:644px;top:42px">Links</div>
  <ul class="abs link-list" style="left:644px;top:72px"><li>Home</li><li>Services</li><li>Team</li><li>Careers</li><li>Blog</li></ul>
  <ul class="abs link-list" style="left:743px;top:72px"><li>Contact us</li><li>Terms and conditions</li><li>Privacy Policy</li><li>Sitemap</li></ul>

  <div class="abs footer-head" style="left:972px;top:42px">Social Media</div>
  <div class="abs social" style="left:972px;top:73px" aria-label="Social media links">
    <span></span><span></span><span></span><span></span>
  </div>
</footer>
<div class="abs footer-rule"></div>
<div class="abs copyright">Copyright &nbsp;© &nbsp;2017 Company name. &nbsp;All rights reserved.</div>

</body>
</html>
```